Navigate the Underground Car Park to 7K3R Vet Clinic

Eye-catching signage for Underground Carpark.
We want to help new Clients, or those with bad senses of direction, to the correct Lift Lobby.
We want to be able to say 'Just follow the signs'.

It can be confusing and many other business have utilised some of the pillars in the carpark to guide their customers to the right place.

People don't want to walk far with sick animals so it is important they get to the right Lift Lobby.
Updates

We are thinking instead of 'Just Follow the Signs,We would like to try:'Looking for us?' (Large Text)'Follow the Signs (much smaller Text)Also, it is very useful to see the proposed sign dropped on to the photo of the car park pillars I included.Many thanks Added Friday, June 16, 2017

Target Market(s)

Customers, coming for the 1st time, trying to navigate the Underground CarPark towards the appropriate Lift lobby

Industry/Entity Type

Veterinary

Font styles to use
Serif

Colors
f78f20
00a990
0455a3

Requirements
Must have
• Logo.
• Bright. Clear. Not too cluttered.
• Warmth. Humour. Approachable.
• Please include: Building 4, Mezzanine Level
Nice to have
• Please look at our FB pages and Instagram page @7k3rvetclinic for a good feel of who we are.
• Some level of style or image continuity with the Pet Tips Poster (see attached file)
Should not have
• Not have a medical feel

```html
<!DOCTYPE html>
<html lang="en">
<head>
<meta charset="utf-8">
<title>7K3R Vet Clinic – Car Park Wayfinding Sign</title>
<link rel="stylesheet" href="https://fonts.googleapis.com/css2?family=Chewy&family=Nunito:ital,wght@0,700;0,800;1,700&display=swap">
<style>
  :root {
    --page-bg: #e4e4e4;
    --cream: #fef7ec;
    --cream-edge: #fbe2c2;
    --orange: #e58f25;
    --orange-bright: #f78f20;
    --teal: #00a990;
    --slate: #2f6b80;
    --blue: #0455a3;
    --ink: #4a4038;
  }
  * { box-sizing: border-box; margin: 0; padding: 0; }
  html, body { width: 1200px; height: 640px; overflow: hidden; }
  body { background: var(--page-bg); position: relative; font-family: "Nunito", sans-serif; }

  .sign {
    position: absolute; left: 385px; top: 26px; width: 430px; height: 588px;
    background: radial-gradient(ellipse at 50% 52%, #fffdf9 0%, var(--cream) 45%, var(--cream-edge) 100%);
    border-left: 4px solid var(--orange); border-right: 4px solid var(--orange);
    border-bottom: 8px solid var(--slate);
    box-shadow: 0 4px 10px rgba(0,0,0,.25);
    overflow: hidden;
  }
  .photo { position: absolute; }
  .photo--parrot { left: 0; top: 0; width: 100px; height: 130px; border-radius: 0 0 50px 0;
    background: linear-gradient(160deg, #f2b11c, #2a74b8 70%, #49a04a); }
  .photo--pug { left: 151px; top: 0; width: 139px; height: 147px; border-radius: 0 0 60px 60px;
    background: radial-gradient(circle at 50% 45%, #f4f1ee, #3a3634 80%); }
  .photo--tabby { left: 303px; top: 26px; width: 121px; height: 125px; border-radius: 40px 0 0 50px;
    background: linear-gradient(200deg, #8c8680, #c9c2b8 60%, #6a645e); }
  .photo--kitten { left: 22px; top: 515px; width: 112px; height: 73px; border-radius: 50px 50px 0 0;
    background: linear-gradient(180deg, #f0b070, #d98a44); }
  .photo--hound { left: 112px; top: 506px; width: 260px; height: 82px; border-radius: 90px 90px 0 0;
    background: linear-gradient(180deg, #b8753e, #3b2a22 55%, #f1ece6); }
  .photo--rabbit { left: 330px; top: 502px; width: 100px; height: 86px; border-radius: 50px 0 0 0;
    background: linear-gradient(180deg, #f6c690, #e7a86a); }

  .paw { position: absolute; border-radius: 50%; background: var(--teal); }
  .paw--a { left: 62px; top: 176px; width: 50px; height: 50px; }
  .paw--b { left: 340px; top: 200px; width: 50px; height: 50px; }
  .paw--c { left: 28px; top: 426px; width: 40px; height: 40px; }
  .paw--d { left: 364px; top: 422px; width: 40px; height: 40px; }

  .brand { position: absolute; left: 0; right: 0; top: 236px;
    display: flex; justify-content: center; align-items: center; gap: 7px; }
  .brand__dot { width: 14px; height: 14px; border-radius: 50%; background: var(--teal); }
  .brand__name { font-weight: 800; font-size: 20px; line-height: 1; color: var(--orange); letter-spacing: .3px; }

  .headline-frame { position: absolute; left: 17px; top: 283px; width: 388px; height: 102px;
    border: 2.5px solid var(--orange); border-radius: 10px; }
  .tagline { position: absolute; left: 0; right: 0; text-align: center; line-height: 1.2; }
  .tagline span { background: #fefaf3; padding: 0 6px; }
  .tagline--clinic { top: 271px; font-style: italic; font-weight: 700; font-size: 19px; color: var(--ink); }
  .headline { position: absolute; left: 17px; width: 388px; top: 308px; text-align: center;
    white-space: nowrap;
    font-family: "Chewy", sans-serif; font-size: 46px; font-weight: 400; line-height: 1;
    color: var(--orange-bright);
    -webkit-text-stroke: 2px var(--blue); paint-order: stroke fill; }
  .tagline--follow { top: 371px; font-weight: 800; font-size: 22px; color: var(--slate); }

  .location { position: absolute; left: 92px; top: 410px; width: 238px; height: 26px;
    background: var(--orange); color: var(--ink); font-weight: 700; font-size: 15px;
    white-space: nowrap;
    display: flex; align-items: center; justify-content: center;
    box-shadow: 0 3px 4px rgba(0,0,0,.2); }

  .direction-arrow { position: absolute; left: 128px; top: 444px; }
</style>
</head>
<body>
  <main class="sign">
    <div class="photo photo--parrot" role="img" aria-label="Photo of a blue and gold macaw peeking in from the top"></div>
    <div class="photo photo--pug" role="img" aria-label="Photo of an upside-down grinning dog"></div>
    <div class="photo photo--tabby" role="img" aria-label="Photo of a tabby cat peeking in"></div>

    <div class="paw paw--a" role="img" aria-label="Teal paw print"></div>
    <div class="paw paw--b" role="img" aria-label="Teal paw print"></div>
    <div class="paw paw--c" role="img" aria-label="Teal paw print"></div>
    <div class="paw paw--d" role="img" aria-label="Teal paw print"></div>

    <div class="brand">
      <span class="brand__dot"></span>
      <span class="brand__name">7K3R Vet Clinic</span>
    </div>

    <div class="headline-frame"></div>
    <p class="tagline tagline--clinic"><span>Veterinary Clinic</span></p>
    <h1 class="headline">Looking for us?</h1>
    <p class="tagline tagline--follow"><span>Follow the Signs</span></p>

    <div class="location">Building 4, Mezzanine Level</div>

    <svg class="direction-arrow" width="166" height="56" viewBox="0 0 166 56" aria-label="Arrow pointing ahead">
      <polygon points="83,0 166,54 0,54" fill="#3a6f84"/>
    </svg>

    <div class="photo photo--kitten" role="img" aria-label="Photo of a ginger kitten"></div>
    <div class="photo photo--hound" role="img" aria-label="Photo of a basset hound with ears flying out"></div>
    <div class="photo photo--rabbit" role="img" aria-label="Photo of a ginger rabbit"></div>
  </main>
</body>
</html>
```